Stationary/business card for Custom Home builder
Pemberton Dwellings General Contractor
Simple
Travis Lindqvist
president
817 Calder Meadow Road
Dorrance Crossing, SC 29871
kbarlowbuilds@mailvero.net
Please use my logo

```html
<!DOCTYPE html>
<html lang="en">
<head>
<meta charset="utf-8">
<title>Pemberton Dwellings General Contractor – Business Card</title>
<link href="https://fonts.googleapis.com/css2?family=Libre+Baskerville:ital@0;1&display=swap" rel="stylesheet">
<style>
  :root {
    --bg: #e4e5e7;
    --card: #ffffff;
    --ink: #2b2b2b;
    --blue: #3f74c9;
    --blue-light: #8fb2e6;
    --blue-dark: #23529f;
    --charcoal: #222326;
    --grey: #9a9ca0;
  }
  * { margin: 0; padding: 0; box-sizing: border-box; }
  html, body { width: 1200px; height: 901px; overflow: hidden; }
  body {
    background: var(--bg);
    font-family: "Libre Baskerville", Georgia, serif;
    color: var(--ink);
    position: relative;
  }
  .card {
    position: absolute;
    top: 296px;
    width: 520px;
    height: 298px;
    background: var(--card);
    box-shadow: 0 6px 20px rgba(0,0,0,0.18);
    overflow: hidden;
  }
  .card--front { left: 60px; }
  .card--back { left: 620px; }

  .company-name {
    position: absolute;
    font-family: "Libre Baskerville", Georgia, serif;
    font-weight: 400;
    color: var(--ink);
    line-height: 1.3;
  }
  .card--front .company-name { left: 40px; top: 40px; font-size: 24px; }
  .card--back .company-name { left: 210px; top: 34px; font-size: 17px; }

  .roofline { position: absolute; }
  .card--front .roofline { left: 0; top: 120px; width: 520px; height: 178px; }
  .card--back .roofline { right: 0; bottom: 0; width: 170px; height: 80px; }

  .name-band {
    position: absolute; left: 0; top: 100px; width: 520px; height: 22px;
    background: linear-gradient(90deg, var(--blue-dark), var(--blue) 55%, var(--blue-light));
    color: #fff; font-style: italic; font-size: 12px;
    display: flex; align-items: center; justify-content: flex-end; padding-right: 40px;
  }
  .name-band__divider { margin: 0 8px; }

  .address, .contact { position: absolute; top: 148px; font-size: 10.5px; line-height: 1.55; font-style: normal; }
  .address { left: 38px; }
  .contact { left: 310px; }

  .stripes { position: absolute; left: 0; bottom: 44px; width: 330px; }
  .stripes__dark { height: 9px; background: var(--charcoal); }
  .stripes__light { height: 4px; background: var(--grey); margin-top: 5px; width: 300px; }
</style>
</head>
<body>
  <section class="card card--front">
    <div class="company-name">Pemberton Dwellings<br>General Contractor</div>
    <svg class="roofline" viewBox="0 0 520 178" role="img" aria-label="Decorative blue rooftop artwork">
      <defs>
        <linearGradient id="roofFill" x1="0" y1="0" x2="1" y2="0">
          <stop offset="0" stop-color="#8fb2e6"/>
          <stop offset="0.5" stop-color="#3f74c9"/>
          <stop offset="1" stop-color="#8fb2e6"/>
        </linearGradient>
      </defs>
      <rect x="0" y="40" width="520" height="138" fill="url(#roofFill)" opacity="0.85"/>
      <rect x="0" y="150" width="520" height="28" fill="#222326"/>
    </svg>
  </section>

  <section class="card card--back">
    <div class="company-name">Pemberton Dwellings<br>General Contractor</div>
    <div class="name-band">Travis Lindqvist<span class="name-band__divider">|</span>president</div>
    <address class="address">
      817 Calder Meadow Road<br>
      Dorrance Crossing, SC 29871
    </address>
    <div class="contact">
      P: 843-555-0172<br>
      F: 843-555-0148<br>
      E: kbarlowbuilds@mailvero.net
    </div>
    <div class="stripes">
      <div class="stripes__dark"></div>
      <div class="stripes__light"></div>
    </div>
    <svg class="roofline" viewBox="0 0 170 80" role="img" aria-label="Decorative blue rooftop artwork">
      <defs>
        <linearGradient id="cornerFill" x1="0" y1="0" x2="1" y2="1">
          <stop offset="0" stop-color="#8fb2e6"/>
          <stop offset="1" stop-color="#3f74c9"/>
        </linearGradient>
      </defs>
      <rect x="0" y="0" width="170" height="80" fill="url(#cornerFill)" opacity="0.85"/>
    </svg>
  </section>
</body>
</html>
```